Business Card Design

I need a business card for my rental business. The business is named:
Hire a Vorlatrike Brenmoor
www.hireavorlatrikebrenmoor.example
(555) 014-2937
This will be a business card that I will leave at other businesses as advertisement so it needs to have the name, website, and phone number.
Please feel free to be creative. This is a new business so I have no designs.
Thank you very much for your time and I look forward to receiving your designs
Target Market(s)
Local rental customers
Industry/Entity Type
Business
Contact Information for Business Card
Please check out my website:
Other font styles liked:
- anything creative
Colors
Designer to choose colors to be used in the design.
Requirements
Must have
- Business name, phone, website. Rentals available hourly or daily. Book online

```html
<!DOCTYPE html>
<html lang="en">
<head>
<meta charset="utf-8">
<title>Hire a Vorlatrike Brenmoor — Business Card</title>
<link rel="stylesheet" href="https://fonts.googleapis.com/css2?family=PT+Sans:wght@700&family=Questrial&display=swap">
<style>
  :root {
    --page: #ffffff;
    --ink: #131313;
    --red: #ec3a36;
    --grey: #a9a9ac;
    --grey-type: #6f6f71;
    --white: #ffffff;
    --faint: #3a3a3a;
    --photo-dark: #3b3b3d;
    --photo-red: #c8342c;
  }
  * { margin: 0; padding: 0; box-sizing: border-box; }
  html, body { width: 1200px; height: 1200px; overflow: hidden; background: var(--page); }
  .sheet { position: relative; width: 1200px; height: 1200px; }

  .card { position: absolute; left: 126px; width: 943px; height: 538px; overflow: hidden; }
  .card--front { top: 60px; background: var(--ink); }
  .card--back { top: 609px; background: var(--ink); }

  .brand-title {
    position: absolute; left: 0; width: 100%; text-align: center;
    font-family: "PT Sans", Tahoma, sans-serif; font-weight: 700;
    font-size: 49px; letter-spacing: -0.5px; line-height: 1; white-space: nowrap;
  }
  .web {
    font-family: "Questrial", "Century Gothic", sans-serif;
    color: var(--white);
  }

  .photo {
    position: absolute; border-radius: 50%; background: var(--white);
    display: flex; align-items: center; justify-content: center;
  }
  .photo__fill {
    width: 78%; height: 46%; border-radius: 40% 40% 30% 30%;
    background: linear-gradient(120deg, var(--photo-dark) 0%, var(--photo-red) 55%, var(--photo-dark) 100%);
  }

  /* front */
  .card--front .photo { left: 406px; top: 170px; width: 122px; height: 122px; }
  .card--front .brand-title { top: 301px; color: var(--white); }
  .front-band { position: absolute; left: 0; top: 352px; width: 100%; height: 20px; background: var(--red); }
  .card--front .web { position: absolute; left: 0; width: 100%; top: 374px; text-align: center; font-size: 26px; }

  /* back */
  .back-top { position: absolute; left: 0; top: 0; width: 100%; height: 311px; background: var(--grey); }
  .swatch { position: absolute; width: 40px; height: 40px; }
  .swatch--red { left: 19px; top: 18px; background: var(--red); }
  .swatch--black { left: 65px; top: 18px; background: var(--ink); }
  .swatch--white { left: 19px; top: 64px; background: var(--white); }
  .card--back .photo { left: 836px; top: 12px; width: 70px; height: 70px; }
  .card--back .brand-title { top: 264px; color: var(--grey-type); }

  .contact { position: absolute; left: 42px; font-family: "Questrial", "Century Gothic", sans-serif; color: var(--white); display: flex; align-items: center; gap: 14px; }
  .contact--phone { top: 410px; font-size: 26px; }
  .contact--web { top: 452px; font-size: 20px; }
  .contact svg { flex: none; }

  .divider { position: absolute; left: 469px; top: 354px; width: 5px; height: 138px; background: var(--red); }
  .offer { position: absolute; left: 487px; font-family: "Questrial", "Century Gothic", sans-serif; color: var(--white); line-height: 1.05; }
  .offer--hours { top: 375px; font-size: 24px; }
  .offer--book { top: 428px; font-size: 22px; }
  .offer__link { color: var(--red); }
  .offer__link .tld { color: var(--white); }
  .footer-web { position: absolute; left: 0; width: 100%; top: 506px; text-align: center; font-family: "Questrial", sans-serif; font-size: 19px; color: var(--faint); }
</style>
</head>
<body>
<main class="sheet">
  <section class="card card--front">
    <div class="photo"><div class="photo__fill" role="img" aria-label="Photo of a red and black three-wheel roadster"></div></div>
    <h1 class="brand-title">HIRE A VORLATRIKE BRENMOOR</h1>
    <div class="front-band"></div>
    <p class="web">www.hireavorlatrikebrenmoor.example</p>
  </section>

  <section class="card card--back">
    <div class="back-top"></div>
    <div class="swatch swatch--red"></div>
    <div class="swatch swatch--black"></div>
    <div class="swatch swatch--white"></div>
    <div class="photo"><div class="photo__fill" role="img" aria-label="Photo of a red and black three-wheel roadster"></div></div>
    <h2 class="brand-title">HIRE A VORLATRIKE BRENMOOR</h2>

    <p class="contact contact--phone">
      <svg width="28" height="28" viewBox="0 0 28 28" aria-hidden="true">
        <circle cx="14" cy="14" r="14" fill="#ec3a36"/>
        <path d="M9 7.5c1-.6 2-.4 2.4.4l1.2 2.4c.3.7 0 1.3-.5 1.7l-.8.6c.7 1.7 2 3.1 3.8 4l.7-.8c.4-.5 1.1-.7 1.7-.4l2.4 1.3c.8.4.9 1.5.3 2.3-.9 1.1-2.3 1.6-3.7 1.1-4-1.5-6.9-4.5-8.3-8.4-.5-1.5.1-3.3 1.6-4.2z" fill="#fff"/>
      </svg>
      (555) 014-2937
    </p>
    <p class="contact contact--web">
      <svg width="26" height="26" viewBox="0 0 26 26" aria-hidden="true">
        <circle cx="13" cy="13" r="13" fill="#ec3a36"/>
        <g fill="none" stroke="#fff" stroke-width="1.4">
          <circle cx="13" cy="13" r="6.5"/>
          <ellipse cx="13" cy="13" rx="3" ry="6.5"/>
          <line x1="6.5" y1="13" x2="19.5" y2="13"/>
        </g>
      </svg>
      www.hireavorlatrikebrenmoor.example
    </p>

    <div class="divider"></div>
    <p class="offer offer--hours">Rentals available hourly or daily</p>
    <p class="offer offer--book">For online bookings,<br>visit <span class="offer__link">www.hireavorlatrikebrenmoor<span class="tld">.example</span></span></p>
    <p class="footer-web">www.hireavorlatrikebrenmoor.example</p>
  </section>
</main>
</body>
</html>
```